Creative Business Card and Stationary set
Brisk Venture
Creative Business Card and Stationary set  - General Merchandise
Creative Brief
Professional
Ilsa Tarn
chief executive officer
no address
ceo@brisk-venture.test
www.brisk-venture.test
We are a company which into different industries: fashion, education, consultancy, etc. We would like a nice modern, clean look and eye catching design that's fitting for a professional firm image. We would like to stick to logo colors, however, designers can change logo color but stick to dark background (black or dark grey) Please use sample information for design purposes. Mainly, we're in need of: - Business card - Letterhead - Envelope - Presentation folder - E-mail signature - Invoice form (Word-based format) - Fax cover (Word-based) - Thank you cards Use icons to indicate phone, fax, mobile, etc. Those are general guidelines and we still open to designers own creative ideas.
we would like to see different versions: 1) Logo and website. 2) Social network address (Pagebook, WorkLoop, Chirrup) 3) Both Please use sample information for design purposes.
farolinu farolinu
Dear Designers Thank you all for your participation and efforts. Wish you good luck in your future projects.
Dear Designers Thank you all for participation. Kindly note that our requirements for this project as stated on the creative brief are as follow: - Business card - Letterhead - Envelope - Presentation folder - E-mail signature - Invoice form (Word-based format) - Fax cover (Word-based) - Thank you cards We will be rating only those provide the full stationary set. Please be creative and don't use templates. Good Luck
Dear Designers Some more nice ideas on how to present information: Social Media and Contact: - http://www.portfolex.test/gallery/Creative-Business-card/20481101 - http://www.portfolex.test/gallery/Creative-Business-Card/20481102 - http://www.portfolex.test/gallery/Tidal-style-Business-Card/20481103 - http://www.portfolex.test/gallery/Nimbo-Tek-Business-Card/20481104
Dear Designers Thank you all for participation and your efforts. We would like to share some ideas as we are looking for new creative design not a typical or a template design. 1) using company name: - http://www.quill-press-hub.test/blog/wp-content/uploads/2013/10/Spot-UV.jpg 2) using initial letters logo BV to create nice decoration: - http://www.dovrenprint.test/store/business-cards/silk-squared - 3) Shadow effects: - http://www.harbeckprinting.test/UV_High_Gloss-16pt_business_cards.html 4) 3D effects: - http://nordvalmaker.files.blogvane.test/2013/04/tk_designs___business_card_by_tkellaway.jpg - http://pemrusk.artgrotto.test/art/Pemrusk-09-Business-Cards-208411730?q=boost%3Apopular+business+cards&qo=181 These are nice ideas along with those links shared previously. Some those ideas might not be applicable using our logo design, here comes the creativity part where you as a designer find away to make it applicable, merge between 2 ideas, try out different colors (some designs might look better if you use other colors), use all ideas to come out with his own new idea, etc. It is all about ideas. Good Luck
Dear Designers Kindly check the following links for nice creative business card ideas: - http://vex7.artgrotto.test/art/Talvor-business-cards-61930284?q=boost%3Apopular+business+cards&qo=82 - http://quarrystudio.artgrotto.test/art/Quarry-Business-Card-93718264?q=boost%3Apopular+business+cards&qo=83 - http://grenvork.artgrotto.test/art/grenvork-Business-Cards-245108837?q=boost%3Apopular+business+cards&qo=95 - http://pemrusk.artgrotto.test/art/Pemrusk-09-Business-Cards-208411730?q=boost%3Apopular+business+cards&qo=181 - http://mapleform.artgrotto.test/art/Tall-Fable-Business-Card-88457193?q=boost%3Apopular+business+cards&qo=185 - http://tivalrunn.artgrotto.test/art/My-new-Business-cards-81693258?q=boost%3Apopular+business+cards&qo=54
Quobit Quobit
Sir, Can you give some star rating please... Thanks.
Dear Designers Please don't use much orange in design. Designers can use a white logo on dark background, they can also use any colors for logo to create nice first impression. Social media links should be included on the card, you can use links or username (use data sample), include them on card back or front, simply do whatever create a nice look. Good Luck

```html
<!DOCTYPE html>
<html lang="en">
<head>
<meta charset="utf-8">
<title>Brisk Venture – Stationery Set</title>
<link href="https://fonts.googleapis.com/css2?family=Montserrat:wght@400;600;700&display=swap" rel="stylesheet">
<style>
:root{
  --bg:#3b3b3b;
  --ink:#242424;
  --paper:#ffffff;
  --accent:#f7941d;
  --muted:#8a8a8a;
  --soft:#e8e8e8;
}
*{box-sizing:border-box;margin:0;padding:0}
html,body{width:1200px;height:228px;overflow:hidden}
body{background:var(--bg);font-family:'Montserrat',Arial,sans-serif;position:relative}
.piece{position:absolute;overflow:hidden}
.paper{background:var(--paper)}
.dark{background:var(--ink)}
.logo{display:flex;align-items:center;gap:2px;font-weight:700;color:var(--ink);white-space:nowrap;text-transform:uppercase;font-size:4px;letter-spacing:.1px}
.logo .mark{background:var(--accent);display:block;width:5px;height:5px;flex:none}
.logo.light{color:var(--paper)}
.name{font-size:4px;font-weight:700;color:var(--ink);white-space:nowrap}
.dark .name{color:var(--paper)}
.role{font-size:3px;color:var(--accent);white-space:nowrap;margin-bottom:2px}
.line{display:flex;align-items:center;gap:1.5px;font-size:3px;line-height:4.2px;color:var(--muted);white-space:nowrap}
.dark .line{color:#cfcfcf}
.line svg{width:3px;height:3px;flex:none;fill:var(--accent)}
.text{font-size:3px;line-height:4.4px;color:var(--muted)}
.rule{position:absolute;left:0;right:0;height:2px;background:var(--accent)}
.wedge{position:absolute;background:var(--accent)}

/* phone */
.phone{left:10px;top:70px;width:26px;height:50px;border-radius:3px;padding:6px 3px}
.phone .logo{font-size:2.6px;justify-content:center;margin-top:12px;gap:1px}
.phone .logo .mark{width:3px;height:3px}
.phone .bar{position:absolute;left:3px;right:3px;bottom:6px;height:2px;background:var(--accent)}

/* business cards */
.card{width:56px;height:32px;border-radius:1px;padding:4px}
.card-a{left:42px;top:60px}
.card-b{left:102px;top:60px}
.card-c{left:42px;top:96px}
.card-d{left:102px;top:96px}
.card-e{left:42px;top:132px}
.card-f{left:102px;top:132px}
.card .logo{margin-top:9px}
.card .wedge{right:0;bottom:0;width:16px;height:32px;clip-path:polygon(100% 0,100% 100%,0 100%)}
.card .info{position:relative;z-index:1}

/* letterheads */
.letter{width:64px;height:86px;padding:5px}
.letter-a{left:166px;top:12px}
.letter-b{left:236px;top:12px}
.letter .body{margin-top:8px}
.letter .foot{position:absolute;left:5px;bottom:5px}
.letter .rule{bottom:0}
.letter .to{margin-top:6px}
.table{margin-top:4px;border-top:1px solid var(--accent)}
.table .row{display:flex;justify-content:space-between;font-size:3px;line-height:4.4px;color:var(--muted);border-bottom:.5px solid var(--soft)}

/* slips */
.slip{width:64px;height:18px;padding:3px 4px}
.slip-a{left:166px;top:108px}
.slip-b{left:236px;top:108px}
.slip .rule{bottom:0}

/* envelopes */
.envelope{width:96px;height:40px;padding:4px}
.env-a{left:310px;top:30px}
.env-a .rule{bottom:0}
.env-a .addr{position:absolute;left:50px;top:18px}
.env-b{left:310px;top:78px}
.env-b .flap{position:absolute;left:0;top:0;width:100%;height:14px;background:var(--accent);clip-path:polygon(0 0,100% 0,50% 100%)}
.env-b .foot{position:absolute;left:4px;bottom:4px}
.compliment{left:310px;top:128px;width:96px;height:18px;padding:3px 4px}
.compliment .rule{bottom:0}

/* disc */
.cd{left:416px;top:32px;width:60px;height:60px;border-radius:50%}
.cd .hole{position:absolute;left:25px;top:25px;width:10px;height:10px;border-radius:50%;background:var(--bg)}
.cd .logo{position:absolute;left:0;right:0;justify-content:center;top:42px;font-size:3px}
.cd .logo .mark{width:4px;height:4px}
.cd-sleeve{left:416px;top:100px;width:60px;height:44px;padding:4px}
.cd-sleeve .wedge{right:0;top:0;width:20px;height:44px;clip-path:polygon(100% 0,100% 100%,0 100%)}

/* folder */
.folder{left:488px;top:20px;width:90px;height:120px;padding:8px}
.folder .logo{font-size:5px}
.folder .logo .mark{width:6px;height:6px}
.folder .wedge{left:0;bottom:0;width:90px;height:50px;clip-path:polygon(0 40%,100% 100%,0 100%)}
.folder .contact{position:absolute;right:6px;bottom:6px;text-align:right}
.folder-inside{left:586px;top:20px;width:90px;height:120px;padding:8px}
.folder-inside .pocket{position:absolute;left:0;right:0;bottom:0;height:40px;background:var(--soft);clip-path:polygon(0 30%,100% 0,100% 100%,0 100%)}
.folder-inside .card-slot{position:absolute;left:50px;bottom:10px;width:30px;height:17px;background:var(--ink);z-index:1;padding:3px}
.folder-inside .card-slot .logo{font-size:2.6px}
.folder-inside .card-slot .logo .mark{width:3px;height:3px}

/* cover */
.cover{left:860px;top:8px;width:330px;height:212px}
.cover .logo{position:absolute;left:178px;top:96px;font-size:13px;gap:5px}
.cover .logo .mark{width:16px;height:16px}
.cover .wedge{right:0;bottom:0;width:90px;height:70px;clip-path:polygon(100% 0,100% 100%,0 100%)}
.cover .band{position:absolute;left:0;bottom:0;width:330px;height:8px;background:var(--ink)}
</style>
</head>
<body>

<svg width="0" height="0" style="position:absolute">
  <defs>
    <symbol id="i-phone" viewBox="0 0 10 10"><path d="M2 0l2.2 2.4-1.2 1.4c.8 1.4 1.8 2.4 3.2 3.2l1.4-1.2L10 8l-1.6 2C4.5 10 0 5.5 0 1.6z"/></symbol>
    <symbol id="i-mail" viewBox="0 0 10 10"><path d="M0 2h10v6H0zM0 2l5 3.5L10 2" stroke="#fff" stroke-width=".6"/></symbol>
    <symbol id="i-web" viewBox="0 0 10 10"><circle cx="5" cy="5" r="5"/></symbol>
    <symbol id="i-pin" viewBox="0 0 10 10"><path d="M5 0a3.6 3.6 0 0 1 3.6 3.6C8.6 6.4 5 10 5 10S1.4 6.4 1.4 3.6A3.6 3.6 0 0 1 5 0z"/></symbol>
  </defs>
</svg>

<div class="piece phone dark">
  <div class="logo light"><span class="mark"></span>Brisk Venture</div>
  <div class="bar"></div>
</div>

<div class="piece card card-a dark"><div class="logo light"><span class="mark"></span>Brisk Venture</div></div>
<div class="piece card card-b paper">
  <div class="info">
    <div class="name">Ilsa Tarn</div>
    <div class="role">Chief Executive Officer</div>
    <div class="line"><svg><use href="#i-phone"/></svg>+00 123 456 789</div>
    <div class="line"><svg><use href="#i-mail"/></svg>ceo@brisk-venture.test</div>
  </div>
  <div class="wedge"></div>
</div>
<div class="piece card card-c paper"><div class="logo"><span class="mark"></span>Brisk Venture</div></div>
<div class="piece card card-d dark">
  <div class="info">
    <div class="name">Ilsa Tarn</div>
    <div class="role">Chief Executive Officer</div>
    <div class="line"><svg><use href="#i-mail"/></svg>ceo@brisk-venture.test</div>
    <div class="line"><svg><use href="#i-web"/></svg>www.brisk-venture.test</div>
  </div>
  <div class="wedge"></div>
</div>
<div class="piece card card-e dark"><div class="logo light"><span class="mark"></span>Brisk Venture</div></div>
<div class="piece card card-f paper">
  <div class="info">
    <div class="line"><svg><use href="#i-phone"/></svg>+00 123 456 789</div>
    <div class="line"><svg><use href="#i-web"/></svg>www.brisk-venture.test</div>
  </div>
  <div class="wedge"></div>
</div>

<div class="piece letter letter-a paper">
  <div class="logo"><span class="mark"></span>Brisk Venture</div>
  <div class="body text">Dear client,<br>Thank you for your trust. We look forward to working with you.</div>
  <div class="foot">
    <div class="line"><svg><use href="#i-mail"/></svg>ceo@brisk-venture.test</div>
    <div class="line"><svg><use href="#i-web"/></svg>www.brisk-venture.test</div>
  </div>
  <div class="rule"></div>
</div>
<div class="piece letter letter-b paper">
  <div class="logo"><span class="mark"></span>Brisk Venture</div>
  <div class="to text">Invoice No. 001</div>
  <div class="table">
    <div class="row"><span>Item</span><span>Total</span></div>
    <div class="row"><span>Service</span><span>000</span></div>
    <div class="row"><span>Design</span><span>000</span></div>
  </div>
  <div class="foot">
    <div class="line"><svg><use href="#i-phone"/></svg>+00 123 456 789</div>
    <div class="line"><svg><use href="#i-mail"/></svg>ceo@brisk-venture.test</div>
  </div>
  <div class="rule"></div>
</div>

<div class="piece slip slip-a paper">
  <div class="logo"><span class="mark"></span>Brisk Venture</div>
  <div class="rule"></div>
</div>
<div class="piece slip slip-b dark">
  <div class="logo light"><span class="mark"></span>Brisk Venture</div>
</div>

<div class="piece envelope env-a paper">
  <div class="logo"><span class="mark"></span>Brisk Venture</div>
  <div class="addr text">To: Client Name</div>
  <div class="rule"></div>
</div>
<div class="piece envelope env-b dark">
  <div class="flap"></div>
  <div class="foot line"><svg><use href="#i-web"/></svg>www.brisk-venture.test</div>
</div>
<div class="piece compliment paper">
  <div class="line"><svg><use href="#i-mail"/></svg>ceo@brisk-venture.test</div>
  <div class="rule"></div>
</div>

<div class="piece cd dark">
  <div class="hole"></div>
  <div class="logo light"><span class="mark"></span>Brisk Venture</div>
</div>
<div class="piece cd-sleeve dark">
  <div class="logo light"><span class="mark"></span>Brisk Venture</div>
  <div class="wedge"></div>
</div>

<div class="piece folder dark">
  <div class="logo light"><span class="mark"></span>Brisk Venture</div>
  <div class="wedge"></div>
  <div class="contact">
    <div class="line"><svg><use href="#i-web"/></svg>www.brisk-venture.test</div>
  </div>
</div>
<div class="piece folder-inside paper">
  <div class="text">Thank you for choosing us.</div>
  <div class="pocket"></div>
  <div class="card-slot"><div class="logo light"><span class="mark"></span>Brisk Venture</div></div>
</div>

<div class="piece cover paper">
  <div class="logo"><span class="mark"></span>Brisk Venture</div>
  <div class="wedge"></div>
  <div class="band"></div>
</div>

</body>
</html>
```